Brindlemoor Realty information card

We need a 5x7 two-sided card to hand out at open houses and provide to our charitable partners for distribution. We are a local real estate group looking to add a "give back" component to our business. We are located in a coastal community and would like to incorporate that feel into our design. We are giving clients who use us the ability to designate 1 out of the 10 charitable organizations we partner with - and we will make a donation to that organization.

We included the 10 partner logos below - we envision them pretty small. Also included 2 photos of the "Brindlemoor" and our logo. Have fun.
Updates

Project Deadline Extended
Reason: We're out of town until Wednesday, May 17th.

Target Market(s)

home buyers & sellers

Industry/Entity Type

Real Estate

Font styles to use
Serif
Sans Serif

Colors

Designer to choose colors to be used in the design.

Requirements
Must have
• slogan & tagline - see attached text file
• Brindlemoor photo
Nice to have
• partner logos - small - maybe in circles?

```html
<!DOCTYPE html>
<html lang="en">
<head>
<meta charset="utf-8">
<title>Brindlemoor Realty – Information Card</title>
<link rel="stylesheet" href="https://fonts.googleapis.com/css2?family=Bebas+Neue&family=Yanone+Kaffeesatz:wght@500&family=Patrick+Hand&family=Ubuntu:wght@500&family=Ubuntu+Condensed&display=swap">
<style>
  :root {
    --page: #d3d3d3;
    --ink: #000000;
    --white: #ffffff;
    --link-blue: #8fb4ff;
    --dusk-top: #7f86a8;
    --dusk-mid: #e98e7e;
    --dusk-glow: #f2a283;
    --shore: #3a3440;
    --sky-top: #6f9fd6;
    --sky-mid: #c9dcef;
    --sea-band: rgba(70, 110, 170, 0.72);
    --headline-grey: #3a3a3a;
    --ring-blue: #3b6fd6;
  }
  * { box-sizing: border-box; margin: 0; padding: 0; }
  html, body { width: 1200px; height: 1200px; overflow: hidden; background: var(--page); }
  .canvas { position: relative; width: 1200px; height: 1200px; }

  .card {
    position: absolute; width: 724px; height: 538px;
    background: var(--ink); overflow: hidden;
  }
  .card--front { left: 112px; top: 40px; }
  .card--back { left: 388px; top: 622px; }

  .photo { position: absolute; left: 0; right: 0; }
  .card--front .photo {
    top: 50px; height: 406px;
    background: linear-gradient(180deg, var(--dusk-top) 0%, var(--dusk-mid) 30%, var(--dusk-glow) 52%, #c8756e 62%, var(--shore) 78%, #2b2a35 100%);
  }
  .card--back .photo {
    top: 50px; height: 395px;
    background: linear-gradient(180deg, var(--sky-top) 0%, var(--sky-mid) 35%, #e8eef5 58%, #7f95ad 70%, #4d5c6a 88%, #6b4c40 100%);
  }

  .crest {
    position: absolute; left: 50%; top: 0; transform: translateX(-50%);
    width: 170px; height: 125px;
  }
  .crest svg { position: absolute; inset: 0; }
  .crest__name {
    position: absolute; left: 0; right: 0; top: 44px;
    font-family: "Ubuntu", sans-serif; font-weight: 500; font-size: 17px;
    color: var(--white); text-align: center; line-height: 1.2;
  }

  .headline {
    position: absolute; left: 0; right: 0; text-align: center;
    font-family: "Bebas Neue", sans-serif; color: var(--white);
    text-shadow: 0 3px 4px rgba(0,0,0,0.55);
  }
  .card--front .headline { top: 132px; font-size: 78px; letter-spacing: -1px; }
  .tagline {
    position: absolute; left: 0; right: 0; top: 222px; text-align: center;
    font-family: "Yanone Kaffeesatz", sans-serif; font-weight: 500; font-size: 32px;
    color: var(--white); text-shadow: 0 2px 3px rgba(0,0,0,0.5);
  }
  .pledge {
    position: absolute; left: 14px; right: 10px; top: 345px; text-align: center;
    font-family: "Patrick Hand", cursive; font-size: 18px; line-height: 1.45;
    color: var(--white); text-shadow: 0 1px 3px rgba(0,0,0,0.8);
  }

  .contact {
    position: absolute; left: 0; right: 0; bottom: 0; height: 82px;
    font-family: "Ubuntu Condensed", sans-serif; font-size: 17px; line-height: 26px;
    color: var(--white);
  }
  .contact__col { position: absolute; top: 16px; }
  .contact__col--left { left: 36px; }
  .contact__col--center { left: 0; right: 0; text-align: center; }
  .contact__col--right { right: 36px; text-align: right; }
  .contact .link { color: var(--link-blue); }
  .contact__col--center .link { font-size: 19px; }

  .card--back .headline {
    top: 120px; font-size: 58px; color: var(--headline-grey);
    text-shadow: 0 0 2px var(--white), 0 2px 3px rgba(255,255,255,0.9), 0 3px 6px rgba(0,0,0,0.35);
  }
  .belief {
    position: absolute; left: 30px; right: 30px; top: 186px; text-align: center;
    font-family: "Patrick Hand", cursive; font-size: 18px; line-height: 1.45; color: var(--ink);
  }
  .promise {
    position: absolute; left: 0; right: 0; top: 262px; height: 155px;
    background: var(--sea-band);
    padding: 12px 80px 0; text-align: center;
    font-family: "Patrick Hand", cursive; font-size: 15.5px; line-height: 1.3; color: var(--white);
    text-shadow: 0 1px 2px rgba(0,0,0,0.6);
  }
  .promise p + p { margin-top: 12px; }

  .partners {
    position: absolute; left: 0; right: 0; bottom: 0; height: 93px;
    display: flex; justify-content: center; align-items: center; gap: 10px;
  }
  .partner {
    width: 58px; height: 58px; border-radius: 50%;
    border: 2px solid var(--ring-blue);
  }
  .partner--1 { background: #d9d9e6; }
  .partner--2 { background: #ffffff; }
  .partner--3 { background: #5d7a5a; }
  .partner--4 { background: #5b4436; }
  .partner--5 { background: #000000; }
  .partner--6 { background: #e78fc6; }
  .partner--7 { background: #1a1a1a; border-color: #ffffff; }
  .partner--8 { background: #ffffff; }
  .partner--9 { background: #d11f2a; }
  .partner--10 { background: #ffffff; }
</style>
</head>
<body>
<main class="canvas">

  <section class="card card--front" aria-label="Card front">
    <div class="photo" role="img" aria-label="Photo of the Brindlemoor coastline at sunset, pink sky over a curved bay and town lights"></div>
    <div class="crest">
      <svg viewBox="0 0 170 125" width="170" height="125" aria-hidden="true"><polygon points="0,0 170,0 170,30 85,125 0,30" fill="#000"/></svg>
      <div class="crest__name">Brindlemoor<br>Realty</div>
    </div>
    <h1 class="headline">Change Homes, Change Lives</h1>
    <p class="tagline">Changing the World One Home at a Time</p>
    <p class="pledge">Because we value generosity and desire to make a difference in our community and world, for every home bought or sold through us, we will make a contribution to one of our amazing partners who are helping to change the world.</p>
    <footer class="contact">
      <div class="contact__col contact__col--left">Owen Hartley<br><span class="link">owen@brindlemoorrealty.com</span></div>
      <div class="contact__col contact__col--center"><span class="link">www.brindlemoorrealty.com</span><br>Harborline Realtors</div>
      <div class="contact__col contact__col--right">Clara Hartley<br><span class="link">clara@brindlemoorrealty.com</span></div>
    </footer>
  </section>

  <section class="card card--back" aria-label="Card back">
    <div class="photo" role="img" aria-label="Photo of a blue sky with clouds above the Brindlemoor hillside, town and ocean, with red flowers in the foreground"></div>
    <div class="crest">
      <svg viewBox="0 0 170 125" width="170" height="125" aria-hidden="true"><polygon points="0,0 170,0 170,30 85,125 0,30" fill="#000"/></svg>
      <div class="crest__name">Brindlemoor<br>Realty</div>
    </div>
    <h2 class="headline">We Live Here. We Give Here.</h2>
    <p class="belief">We give because we value generosity and believe we have been blessed to be a blessing.<br>We believe that together we can change the world one home at a time.</p>
    <div class="promise">
      <p>You have our guarantee of personal service and no additional costs. The donations come out of our commission, not your pocket. You get to designate which of our amazing partner organizations you would like us to contribute to on behalf of your transaction.</p>
      <p>When you are ready to buy or sell, please consider giving us a call. Tell a friend about us too. Together, we can make the world a better place.</p>
    </div>
    <ul class="partners" aria-label="Partner organizations">
      <li class="partner partner--1" style="list-style:none"></li>
      <li class="partner partner--2" style="list-style:none"></li>
      <li class="partner partner--3" style="list-style:none"></li>
      <li class="partner partner--4" style="list-style:none"></li>
      <li class="partner partner--5" style="list-style:none"></li>
      <li class="partner partner--6" style="list-style:none"></li>
      <li class="partner partner--7" style="list-style:none"></li>
      <li class="partner partner--8" style="list-style:none"></li>
      <li class="partner partner--9" style="list-style:none"></li>
      <li class="partner partner--10" style="list-style:none"></li>
    </ul>
  </section>

</main>
</body>
</html>
```